Layout for new page on existing website

We have an existing website (www.brightmillworks.org) and need a new page designing to promote a new product.
The new page needs to be consistent with the existing website look and feel (www.brightmillworks.org) but current persistent elements on the standard page design can be moved/removed from the page to accommodate a new layout necessary for getting all the content laid out in a logical user friendly way.
The content required for the page is attached along with a wireframe mock up that may help understand the expectation, however the wireframe was just created to help me work out what was needed on the page and the layout can be different. A key element is the quality of the design of each of the artifacts (e.g. the panel the embedded video needs to go in, icons etc) and a clear display of the information.
Updates
The website that the new page needs to fit into is www.brightmillworks.org, i will also added the company logo to the brief.
Our Corporate Colours
- Green: #A2FF00
- Cream: #FFFF99
- Yellow: #FFE900
- Grey: #534741

```html
<!DOCTYPE html>
<html lang="en">
<head>
<meta charset="utf-8">
<title>Course Booking System</title>
<link href="https://fonts.googleapis.com/css2?family=Fira+Sans+Extra+Condensed:ital,wght@0,400;0,500;1,400;1,500&display=swap" rel="stylesheet">
<style>
  :root {
    --grey: #534741;
    --olive: #8f8e5c;
    --olive-dark: #8a8955;
    --rule: #5b5047;
    --yellow: #f7f243;
    --white: #ffffff;
    --field: #8f8e5c;
  }
  html, body { margin: 0; padding: 0; }
  body {
    width: 1038px; height: 1200px; overflow: hidden;
    background: var(--grey);
    font-family: "Fira Sans Extra Condensed", "Arial Narrow", sans-serif;
    position: relative;
  }
  .page { position: absolute; left: 155px; top: 0; width: 873px; height: 1200px; }
  .panel {
    position: absolute; left: 0; width: 873px;
    background: var(--olive);
    border-top: 2px solid var(--rule);
    box-sizing: border-box;
  }
  .panel--features { top: 0; height: 176px; }
  .panel--venue { top: 176px; height: 175px; }
  .panel--benefits { top: 351px; height: 555px; border-bottom: 3px solid var(--rule); }
  .panel--contact { top: 906px; height: 291px; background: var(--white); border: none; left: 2px; width: 871px; }

  .feature { position: absolute; }
  .feature__icon { position: absolute; left: 0; top: 0; width: 38px; height: 38px; }
  .feature__title {
    position: absolute; margin: 0; white-space: nowrap;
    font-style: italic; font-weight: 400; font-size: 25px; color: var(--yellow);
  }
  .feature__text {
    position: absolute; margin: 0;
    font-style: italic; font-size: 14px; line-height: 25px; color: var(--white);
  }

  .benefits__title {
    position: absolute; left: 54px; top: 6px; margin: 0;
    font-variant: small-caps; font-weight: 500; font-size: 38px; color: var(--yellow);
  }
  .benefits__list {
    position: absolute; left: 53px; top: 80px; margin: 0; padding: 0; list-style: none;
    font-style: italic; font-size: 14px; line-height: 31px; color: var(--white);
  }
  .benefits__list li { padding-left: 28px; position: relative; width: 740px; }
  .benefits__list li.has-mark::before { content: ">>"; position: absolute; left: 0; }

  .contact__title {
    position: absolute; left: 31px; top: 28px; margin: 0; white-space: nowrap;
    font-variant: small-caps; font-weight: 500; font-size: 30px; color: var(--olive-dark);
    letter-spacing: 0.3px;
  }
  .contact__label {
    position: absolute; left: 32px;
    font-variant: small-caps; font-weight: 500; font-size: 21px; color: var(--olive-dark);
  }
  .contact__field {
    position: absolute; left: 142px; width: 366px; height: 23px;
    border: 1px solid var(--field); box-sizing: border-box; background: var(--white);
  }
  .contact__submit {
    position: absolute; left: 592px; top: 231px; width: 117px; height: 54px;
    border: none; border-radius: 10px; background: var(--olive-dark); color: var(--white);
    font-family: inherit; font-variant: small-caps; font-weight: 500; font-size: 22px;
  }
</style>
</head>
<body>
<main class="page">
  <section class="panel panel--features">
    <div class="feature" style="left:28px; top:19px;">
      <svg class="feature__icon" viewBox="0 0 38 38" aria-hidden="true">
        <rect x="3" y="4" width="32" height="23" rx="2" fill="#d9e4ee" stroke="#6f7e8a"/>
        <rect x="6" y="7" width="26" height="17" fill="#3a8fd6"/>
        <rect x="15" y="27" width="8" height="5" fill="#a8b4bd"/>
        <rect x="10" y="32" width="18" height="3" rx="1" fill="#c7d0d6"/>
      </svg>
      <h2 class="feature__title" style="left:54px; top:6px;">Customisable look and feel</h2>
      <p class="feature__text" style="left:7px; top:51px; width:360px;">All elements of the booking systems design will fit in with your existing websites style.</p>
    </div>
    <div class="feature" style="left:490px; top:19px;">
      <svg class="feature__icon" viewBox="0 0 38 38" aria-hidden="true">
        <circle cx="17" cy="17" r="15" fill="#2f6fc4" stroke="#1d3f78"/>
        <path d="M7 12 Q13 8 17 13 Q15 20 10 22 Z M20 7 Q27 9 28 17 Q23 18 21 13 Z" fill="#6fb24a"/>
        <path d="M16 26 L22 32 L35 17" fill="none" stroke="#5cc22b" stroke-width="5" stroke-linecap="round" stroke-linejoin="round"/>
      </svg>
      <h2 class="feature__title" style="left:48px; top:2px;">Live course place availability</h2>
      <p class="feature__text" style="left:10px; top:48px; width:340px; text-align:justify;">By defining minimum and maximum candidates permitted on a course its easy to prevent overbooking and also prevent courses running that don’t have enough candidates.</p>
    </div>
  </section>

  <section class="panel panel--venue">
    <div class="feature" style="left:28px; top:25px;">
      <svg class="feature__icon" viewBox="0 0 38 38" aria-hidden="true">
        <rect x="1" y="6" width="34" height="30" fill="#f4f4f4" stroke="#8a8a8a"/>
        <rect x="4" y="12" width="22" height="14" fill="#7ab85a"/>
        <rect x="4" y="12" width="22" height="6" fill="#8cc4e8"/>
        <path d="M28 2 v10 M23 7 h10" stroke="#3aa52a" stroke-width="3"/>
        <path d="M24 18 l8 8 M32 18 l-8 8" stroke="#d8262a" stroke-width="3"/>
        <path d="M27 29 l2 4 l4 -5" stroke="#3a6fc4" stroke-width="2" fill="none"/>
      </svg>
      <h2 class="feature__title" style="left:66px; top:6px;">Venue database management</h2>
      <p class="feature__text" style="left:7px; top:63px; width:360px;">Easily add, edit and remove venues from which you operate your courses from.</p>
    </div>
  </section>

  <section class="panel panel--benefits">
    <h2 class="benefits__title">Key Benefits</h2>
    <ul class="benefits__list">
      <li class="has-mark">Live Availability – Availability on course place availability to prevent overbooking</li>
      <li>Customers can search for Courses and Book Online with immediate confirmation</li>
      <li class="has-mark">Automated confirmation emails</li>
      <li class="has-mark">Be available for business 24/7 and take orders anytime! Customers can book whe&nbsp; it’s most convenient for them – be it early morning, late evening or weekend</li>
      <li class="has-mark">No fielding phone calls, no wading through paper registrations. Attendees book onyour website, there and then</li>
      <li class="has-mark">No more trips to the bank, take immediate and secure payments online</li>
      <li class="has-mark">Automated confirmation emails so reducing the time need communicating with candidates</li>
      <li class="has-mark">Boost course bookings and reduce administrative time and costs</li>
      <li class="has-mark">Course Admin is Web based meaning you can access your course information from anywhere at any time.</li>
      <li class="has-mark">System is very intuitive and easy to use.</li>
      <li class="has-mark">Lighten your workload</li>
      <li class="has-mark">Upload and manage offline bookings through the admin dashboard</li>
      <li class="has-mark">Keep your attendees organized all the way up to the course date and beyond</li>
    </ul>
  </section>

  <section class="panel panel--contact">
    <h2 class="contact__title">Contact Us Now for a free no obligation discussion</h2>
    <span class="contact__label" style="top:76px;">Name</span>
    <div class="contact__field" style="top:80px;"></div>
    <span class="contact__label" style="top:114px;">Company</span>
    <div class="contact__field" style="top:122px;"></div>
    <span class="contact__label" style="top:151px;">Email</span>
    <div class="contact__field" style="top:159px;"></div>
    <span class="contact__label" style="top:188px;">Telephone</span>
    <div class="contact__field" style="top:193px;"></div>
    <button class="contact__submit" type="button">Submit</button>
  </section>
</main>
</body>
</html>
```